New Business Card Design Project

Make a kick ass business card for The Otter Tea Mug, using the designs. I also might like the 2nd place design logo on the back? Maybe all black with that? Not sure. Also, I'm cool with it being on metal, plastic, glass? or whatever for the business card. Maybe shaped like a shark? Let me know what else you need? Would like designs in the next day or so. Thank you.
Target Market(s)
Anyone that is cool
Contact Information for Business Card
Name: Dorian Fenwick
Phone: 317.594.8126
inventor/creator/entrepreneur/owner
www.theottertyeamug.example
social media links
https://www.facebook.com/theottertyeamug
https://twitter.com/otter_brew
https://www.instagram.com/theottertyeamug/
I'll get the Pinterest one soon
Colors
Designer to choose colors to be used in the design.
Requirements
Must have
- The Otter Tea Mug
- www.theottertyeamug.example
- social media tags?
- My logos and picture/photo of wine glass
Nice to have
- Maybe shaped like a wine glass or shark
- I'll let you decide but my same colors from my website would be nice

```html
<!DOCTYPE html>
<html lang="en">
<head>
<meta charset="utf-8">
<title>Otter Tea Mug – Business Card</title>
<link href="https://fonts.googleapis.com/css2?family=Montserrat:wght@400;500&family=Questrial&family=Sacramento&display=swap" rel="stylesheet">
<style>
  :root {
    --page-bg: #ffffff;
    --card-bg: #161616;
    --glass-tone-a: rgba(214, 166, 106, 0.10);
    --glass-tone-b: rgba(214, 166, 106, 0.03);
    --glass-edge: rgba(214, 166, 106, 0.35);
    --text-light: #d2d2d2;
    --text-white: #f2f2f2;
    --label-red: #7a2226;
  }
  * { margin: 0; padding: 0; box-sizing: border-box; }
  html, body {
    width: 1200px; height: 1000px; overflow: hidden;
    background: var(--page-bg);
  }
  .canvas { position: relative; width: 1200px; height: 1000px; }

  .card {
    position: absolute; top: 138px;
    width: 392px; height: 724px;
    background: var(--card-bg);
  }
  .card--front { left: 156px; }
  .card--back  { left: 654px; }

  .glass-art {
    position: absolute; left: 60px; top: 67px;
    width: 272px; height: 634px;
    border-radius: 40px 40px 120px 120px;
    background: linear-gradient(180deg, var(--glass-tone-a), var(--glass-tone-b));
    border: 1.5px solid var(--glass-edge);
  }

  .brand-name {
    position: absolute; left: 0; right: 0; top: 324px;
    text-align: center;
    font-family: "Questrial", sans-serif;
    font-size: 23px; color: var(--text-light);
    letter-spacing: -0.2px;
  }

  .holder {
    position: absolute; left: 0; right: 0; top: 240px;
    text-align: center;
  }
  .holder__name {
    font-family: "Sacramento", cursive;
    font-size: 30px; line-height: 1; color: var(--text-white);
    letter-spacing: 4px;
  }
  .holder__role {
    margin-top: 1px;
    font-family: "Montserrat", sans-serif;
    font-size: 7.5px; letter-spacing: 1.2px; color: var(--text-white);
  }

  .contact {
    position: absolute; left: 0; right: 0;
    display: flex; justify-content: center; align-items: center; gap: 6px;
    font-family: "Montserrat", sans-serif;
    font-size: 8px; letter-spacing: 1px; color: var(--text-white);
  }
  .contact--phone { top: 311px; }
  .contact--web   { top: 336px; }
  .contact svg { width: 9px; height: 9px; fill: var(--text-white); }

  .side-label {
    position: absolute; top: 890px; width: 392px;
    text-align: center;
    font-family: "Montserrat", sans-serif;
    font-size: 29px; letter-spacing: 4px; color: var(--label-red);
  }
  .side-label--front { left: 156px; }
  .side-label--back  { left: 654px; }
</style>
</head>
<body>
<main class="canvas">
  <section class="card card--front">
    <div class="glass-art" role="img" aria-label="Gold line drawing of a wine glass outline"></div>
    <div class="brand-name">Otter Tea Mug</div>
  </section>

  <section class="card card--back">
    <div class="glass-art" role="img" aria-label="Gold line drawing of a wine glass outline"></div>
    <div class="holder">
      <div class="holder__name">Dorian Fenwick</div>
      <div class="holder__role">Creator / Entrepreneur / Owner</div>
    </div>
    <div class="contact contact--phone">
      <svg viewBox="0 0 24 24" aria-hidden="true"><path d="M6.6 10.8c1.4 2.8 3.8 5.1 6.6 6.6l2.2-2.2c.3-.3.7-.4 1-.2 1.1.4 2.3.6 3.6.6.6 0 1 .4 1 1V20c0 .6-.4 1-1 1C10.6 21 3 13.4 3 4c0-.6.4-1 1-1h3.5c.6 0 1 .4 1 1 0 1.3.2 2.5.6 3.6.1.3 0 .7-.2 1l-2.3 2.2z"/></svg>
      <span>317.594.8126</span>
    </div>
    <div class="contact contact--web">
      <svg viewBox="0 0 24 24" aria-hidden="true"><path d="M12 2a10 10 0 1 0 0 20 10 10 0 0 0 0-20zm6.9 6h-3a15 15 0 0 0-1.3-3.9A8 8 0 0 1 18.9 8zM12 4c.8 1.2 1.5 2.5 1.9 4h-3.8c.4-1.5 1.1-2.8 1.9-4zM4.3 14a8 8 0 0 1 0-4h3.4a16 16 0 0 0 0 4H4.3zm.8 2h3a15 15 0 0 0 1.3 3.9A8 8 0 0 1 5.1 16zm3-8h-3a8 8 0 0 1 4.3-3.9C8.8 5.3 8.4 6.6 8.1 8zM12 20c-.8-1.2-1.5-2.5-1.9-4h3.8c-.4 1.5-1.1 2.8-1.9 4zm2.3-6H9.7a14 14 0 0 1 0-4h4.6a14 14 0 0 1 0 4zm.3 5.9c.6-1.2 1-2.5 1.3-3.9h3a8 8 0 0 1-4.3 3.9zM16.3 14a16 16 0 0 0 0-4h3.4a8 8 0 0 1 0 4h-3.4z"/></svg>
      <span>www.theottertyeamug.example</span>
    </div>
  </section>

  <div class="side-label side-label--front">Front</div>
  <div class="side-label side-label--back">Back</div>
</main>
</body>
</html>
```